Visitenkarten-Design für Persisches Restaurant
Zielgruppe
persisches Restaurant, suche ein Hochwertiges Design für internationale Kunden
Aufgabenstellung
möchte eine hochwertige und elegante visitenkarte
auf der Vorderseite sollte das Logo sein und auf der Rückseite Öffnungszeit, Adresse, Tel. E-Mail und homepage

```html
<!DOCTYPE html>
<html lang="de">
<head>
<meta charset="utf-8">
<title>Golnar – Visitenkarte</title>
<link href="https://fonts.googleapis.com/css2?family=Cormorant+Garamond:ital,wght@0,500;0,600;0,700;1,600&display=swap" rel="stylesheet">
<style>
  :root {
    --backdrop: #eeeeee;
    --card: #ffffff;
    --ink: #2a2a2a;
    --ink-soft: #3a3a3a;
    --rule: #2f2f2f;
    --shadow: rgba(0, 0, 0, 0.12);
  }
  html, body {
    margin: 0;
    padding: 0;
    width: 1200px;
    height: 864px;
    overflow: hidden;
    background: var(--backdrop);
  }
  .stage {
    width: 1200px;
    height: 864px;
    display: flex;
    align-items: center;
    justify-content: center;
    gap: 48px;
  }
  .card {
    width: 500px;
    height: 323px;
    background: var(--card);
    box-shadow: 0 6px 18px var(--shadow);
    display: flex;
    flex-direction: column;
    align-items: center;
    justify-content: center;
    font-family: "Cormorant Garamond", Georgia, serif;
    color: var(--ink);
    box-sizing: border-box;
  }
  .card-back { text-align: center; }
  .hours-title {
    font-weight: 700;
    font-size: 22px;
    margin: 0 0 2px;
  }
  .hours-line {
    font-weight: 500;
    font-size: 24px;
    margin: 0;
    line-height: 1.15;
  }
  .divider {
    width: 250px;
    height: 1.5px;
    background: var(--rule);
    margin: 12px 0 10px;
  }
  .address {
    font-weight: 500;
    font-size: 16px;
    margin: 0 0 4px;
    color: var(--ink-soft);
  }
  .online {
    font-weight: 600;
    font-style: italic;
    font-size: 20px;
    margin: 0;
  }
  .brand {
    display: flex;
    align-items: center;
    gap: 14px;
  }
  .brand-mark {
    width: 18px;
    height: 18px;
    border-radius: 50%;
    background: var(--ink);
  }
  .brand-name {
    font-weight: 600;
    font-size: 58px;
    letter-spacing: 2px;
    color: var(--ink);
  }
</style>
</head>
<body>
<main class="stage">
  <section class="card card-back">
    <p class="hours-title">Öffnungszeiten:</p>
    <p class="hours-line">Mon - Fri 11:30 - 22:30</p>
    <p class="hours-line">Sat - Sun 12:00 - 22:30</p>
    <div class="divider"></div>
    <p class="address">Gartenstr. 7 · 60594 Frankfurt · T.: +49 69 480215</p>
    <p class="online">www.golnar-kueche.de · info@golnar-kueche.de</p>
  </section>
  <section class="card card-front">
    <div class="brand">
      <span class="brand-mark"></span>
      <span class="brand-name">GOLNAR</span>
    </div>
  </section>
</main>
</body>
</html>
```